Larkwell Moments Studio Website
looking for wow/drama
Larkwell Moments Studio Website - Events
Creative Brief
Events
www.larkwellmoments.example
Based in Greater Boston, Larkwell Moments Studio is a boutique custom events and marketing firm.
Looking for dramatic layout/bold. Clean and simple...DRAMA/showstopper! I like texture would prefer navigation to be unique - located in a new place/different layout -- unexpected I WANT A VERY UNIQUE LAYOUT Don't like: anything ordinary/hate wehn things feel "flat"
Black
Teal (the exact teal of my logo)
White and dark Grey accents (from my logo)
right side
http://www.doranpeswick.example/
http://www.thebrightorchard.example/
http://www.velvetaffairs.example.uk/
drama wins. I will not have much "copy" cluttering up my website, The look of the website needs to be a showstopper. other websites: http://www.zintrova.example.uk/ (unique layout) http://www.quillmarshband.example.uk/index4.php http://www.brantoloft.example/

```html
<!DOCTYPE html>
<html lang="en">
<head>
<meta charset="utf-8">
<title>Larkwell Moments Studio</title>
<link rel="stylesheet" href="https://fonts.googleapis.com/css2?family=Cinzel:wght@400&family=PT+Sans:wght@400&display=swap">
<style>
  :root {
    --page: #ffffff;
    --ink-deep: #08212b;
    --panel: rgba(10, 36, 46, 0.72);
    --nav-band: rgba(12, 40, 50, 0.55);
    --text-light: #e3eff0;
    --text-muted: #cfe1e3;
  }
  * { margin: 0; padding: 0; box-sizing: border-box; }
  html, body {
    width: 1200px;
    height: 914px;
    overflow: hidden;
    background: var(--page);
  }
  .site {
    position: absolute;
    left: 55px;
    top: 38px;
    width: 1110px;
    height: 830px;
    overflow: hidden;
    background: var(--ink-deep);
  }
  .site-backdrop {
    position: absolute;
    inset: 0;
    width: 100%;
    height: 100%;
  }
  .brand-panel {
    position: absolute;
    left: 0;
    top: 142px;
    width: 457px;
    height: 232px;
    background: var(--panel);
    display: flex;
    align-items: center;
    padding-left: 32px;
  }
  .brand-mark {
    flex: none;
    width: 16px;
    height: 16px;
    border-radius: 50%;
    background: var(--text-light);
    margin-right: 14px;
  }
  .brand-name {
    font-family: "PT Sans", sans-serif;
    font-weight: 400;
    font-size: 34px;
    line-height: 1.2;
    color: var(--text-light);
    white-space: nowrap;
  }
  .intro {
    position: absolute;
    left: 302px;
    top: 484px;
    width: 790px;
    font-family: "PT Sans", sans-serif;
    font-weight: 400;
    font-size: 20px;
    line-height: 36px;
    color: var(--text-muted);
  }
  .intro-line {
    display: block;
    white-space: nowrap;
  }
  .main-nav {
    position: absolute;
    left: 0;
    top: 737px;
    width: 1110px;
    height: 56px;
    background: linear-gradient(90deg, rgba(12,40,50,0.2), var(--nav-band) 20%, var(--nav-band) 80%, rgba(12,40,50,0.2));
  }
  .main-nav ul { list-style: none; }
  .main-nav li {
    position: absolute;
    top: 17px;
    font-family: "Cinzel", serif;
    font-size: 17px;
    letter-spacing: 0.5px;
    color: var(--text-light);
    text-transform: uppercase;
    white-space: nowrap;
  }
  .nav-home { left: 45px; }
  .nav-business { left: 207px; }
  .nav-gatherings { left: 507px; }
  .nav-contact { left: 795px; }
</style>
</head>
<body>
  <main class="site">
    <svg class="site-backdrop" viewBox="0 0 1110 830" preserveAspectRatio="none" role="img" aria-label="Textured teal photographic backdrop with faint silhouettes of guests and a sparkling light burst">
      <defs>
        <radialGradient id="glow-top" cx="0.6" cy="0.35" r="0.6">
          <stop offset="0" stop-color="#3f8a92"/>
          <stop offset="0.55" stop-color="#1f5a66"/>
          <stop offset="1" stop-color="#0b2a35"/>
        </radialGradient>
        <radialGradient id="glow-low" cx="0.15" cy="0.85" r="0.4">
          <stop offset="0" stop-color="#5fa7ad" stop-opacity="0.55"/>
          <stop offset="1" stop-color="#5fa7ad" stop-opacity="0"/>
        </radialGradient>
        <radialGradient id="sparkle" cx="0.5" cy="0.5" r="0.5">
          <stop offset="0" stop-color="#e6f4f5" stop-opacity="0.7"/>
          <stop offset="1" stop-color="#e6f4f5" stop-opacity="0"/>
        </radialGradient>
      </defs>
      <rect width="1110" height="830" fill="url(#glow-top)"/>
      <rect width="1110" height="830" fill="url(#glow-low)"/>
      <circle cx="880" cy="380" r="120" fill="url(#sparkle)"/>
    </svg>

    <header class="brand-panel">
      <span class="brand-mark"></span>
      <h1 class="brand-name">Larkwell Moments Studio</h1>
    </header>

    <section class="intro">
      <p>
        <span class="intro-line">Lorem ipsum dolor sit amet, ei mutat simul cum. Vim ut democritum dissentiunt,</span>
        <span class="intro-line">in saepe sanctus voluptatibus qui, at his iudico lobortis iudicabit.</span>
      </p>
      <p><span class="intro-line">Ex vocent tritani pro, homero perfecto sea ad.</span></p>
      <p>
        <span class="intro-line">Cibo labores an per, ut dicant quaestio praesent eam, qui ex choro indoctum</span>
        <span class="intro-line">conclusionemque.</span>
      </p>
    </section>

    <nav class="main-nav">
      <ul>
        <li class="nav-home">Home</li>
        <li class="nav-business">Business Services</li>
        <li class="nav-gatherings">Home Gatherings</li>
        <li class="nav-contact">Contact LMS</li>
      </ul>
    </nav>
  </main>
</body>
</html>
```